Postcard design to acquire new clients for my Property Management Company

I'm looking for a postcard design that I can send to prospective clients detailing information about my company and services.
Postcard should be eye catching and contain information from www.brightkeyrentals-example.com. I've provided a few screen shots for the most important information and my logo.
Target Market(s)
Real Estate
Industry/Entity Type
Real Estate
Font styles to use
Sans Serif
Requirements
Must have
- Must be eye catching!! this will be a direct mail piece - I'd like for the card to be read and not tossed in the trash immediately.
Design que from the logo.
A place to write / print the receipts name and address.
our physical address - 2287 Marble Lane, Lubbock, TX 79555.
Should not have
- the contact information on the business card is not accurate - please use info from website.

```html
<!DOCTYPE html>
<html lang="en">
<head>
<meta charset="utf-8">
<title>BrightKey Property Management Postcard</title>
<link href="https://fonts.googleapis.com/css2?family=Montserrat:wght@300;400;500;700;800&display=swap" rel="stylesheet">
<style>
:root{
  --navy:#0d4a86;
  --navy-deep:#0a3f74;
  --grey:#a7a7a7;
  --paper:#ffffff;
  --backdrop:#c4c4c4;
  --ink:#0d4a86;
  --muted:#8a8a8a;
  --sky:#8fb3d6;
  --facade:#c9ced1;
}
*{margin:0;padding:0;box-sizing:border-box}
html,body{width:1200px;height:1200px;overflow:hidden;background:var(--backdrop);font-family:"Montserrat",sans-serif}
.sheet{position:relative;width:1200px;height:1200px}
.card{position:absolute;left:187px;width:826px;height:551px;background:var(--paper);overflow:hidden;box-shadow:0 4px 14px rgba(0,0,0,.18)}
.card--front{top:29px}
.card--back{top:620px}
.card-shapes{position:absolute;inset:0;width:100%;height:100%}
.brand{position:absolute;color:var(--ink)}
.brand-name{font-weight:700;font-size:29px;letter-spacing:5px;line-height:1}
.brand-tag{font-weight:400;font-size:13px;letter-spacing:3.4px;margin-top:6px}
.card--front .brand{left:25px;top:42px}
.card--back .brand{left:56px;top:38px;color:#fff}
.headline{position:absolute;left:40px;top:212px;color:#fff;font-size:38px;line-height:48px}
.headline .light{font-weight:300}
.headline .bold{font-weight:700}
.tagline{position:absolute;left:27px;top:506px;color:var(--muted);font-size:12.5px;line-height:17px;letter-spacing:.3px}
.services-title{position:absolute;left:58px;top:128px;color:#fff;font-weight:700;font-size:20px;letter-spacing:.3px}
.services-sub{position:absolute;left:58px;top:155px;color:#fff;font-size:12px;line-height:16px;letter-spacing:.3px}
.service{position:absolute;display:flex;align-items:center;gap:10px;color:#fff;font-size:14px;line-height:18px;letter-spacing:.3px}
.service svg{width:62px;height:62px;flex:none}
.stamp-box{position:absolute;left:670px;top:92px;width:96px;height:96px;border:1.5px solid #333}
.address-line{position:absolute;left:530px;width:236px;border-top:1.5px solid #333}
.contact{position:absolute;left:516px;top:376px;width:290px;text-align:center;color:#111}
.contact-title{color:var(--ink);font-weight:800;font-size:22px;line-height:28px;margin-bottom:8px}
.contact-line{font-size:13px;line-height:19px;white-space:nowrap}
</style>
</head>
<body>
<main class="sheet">

  <section class="card card--front">
    <svg class="card-shapes" viewBox="0 0 826 551" preserveAspectRatio="none">
      <defs>
        <linearGradient id="photoTone" x1="0" y1="0" x2="0" y2="1">
          <stop offset="0" stop-color="var(--sky)"/>
          <stop offset=".35" stop-color="var(--facade)"/>
          <stop offset=".85" stop-color="#a9adae"/>
          <stop offset="1" stop-color="#8a7a6a"/>
        </linearGradient>
      </defs>
      <polygon points="333,0 440,0 318,168" fill="var(--grey)"/>
      <polygon points="440,0 826,0 826,412 470,530 300,170" fill="url(#photoTone)" role="img" aria-label="Photo of a modern curved office building with glass windows"/>
      <polygon points="0,128 525,222 430,440 0,495" fill="var(--navy)"/>
      <polygon points="400,222 525,222 430,440" fill="var(--navy)" opacity=".55"/>
      <polygon points="0,495 470,430 360,551 0,551" fill="var(--paper)"/>
      <polygon points="360,551 826,415 826,551" fill="var(--navy)"/>
    </svg>
    <div class="brand">
      <div class="brand-name">BRIGHTKEY</div>
      <div class="brand-tag">PROPERTY MANAGEMENT</div>
    </div>
    <h1 class="headline">
      <span class="light">CHOOSE THE</span><br>
      <span class="bold">RIGHT PROPERTY</span><br>
      <span class="bold">MANAGEMENT</span><br>
      <span class="light">SYSTEM</span>
    </h1>
    <p class="tagline">SELECTING THE WRONG MANAGER<br>COULD BE YOUR COSTLIEST MISTAKE EVE</p>
  </section>

  <section class="card card--back">
    <svg class="card-shapes" viewBox="0 0 826 551" preserveAspectRatio="none" aria-hidden="true">
      <polygon points="0,0 528,0 428,551 0,551" fill="var(--navy)"/>
    </svg>
    <div class="brand">
      <div class="brand-name">BRIGHTKEY</div>
      <div class="brand-tag">PROPERTY MANAGEMENT</div>
    </div>
    <h2 class="services-title">DISCOVER OUR SERVICES</h2>
    <p class="services-sub">WE OFFER FULL-SERVICE PROPERTY<br>MANAGEMENT SOLUTIONS</p>

    <div class="service" style="left:56px;top:216px">
      <svg viewBox="0 0 62 62"><circle cx="31" cy="31" r="29" fill="none" stroke="#fff" stroke-width="2.5"/><path d="M17 32 L31 19 L45 32 M21 29 V44 H28 V36 H34 V44 H41 V29" fill="none" stroke="#fff" stroke-width="3" stroke-linejoin="round"/></svg>
      <span>Property<br>Marketing</span>
    </div>
    <div class="service" style="left:258px;top:216px">
      <svg viewBox="0 0 62 62"><circle cx="31" cy="31" r="29" fill="none" stroke="#fff" stroke-width="2.5"/><circle cx="28" cy="27" r="10" fill="none" stroke="#fff" stroke-width="3"/><path d="M35 34 L45 44" stroke="#fff" stroke-width="4.5" stroke-linecap="round"/></svg>
      <span>Property<br>Inspections</span>
    </div>
    <div class="service" style="left:56px;top:295px">
      <svg viewBox="0 0 62 62"><circle cx="31" cy="31" r="29" fill="none" stroke="#fff" stroke-width="2.5"/><circle cx="26" cy="25" r="6" fill="#fff"/><circle cx="37" cy="24" r="5" fill="#fff"/><path d="M15 44 C15 34 37 34 37 44 Z M34 33 C42 31 48 35 48 42 H39" fill="#fff"/></svg>
      <span>Tenant<br>Screening</span>
    </div>
    <div class="service" style="left:258px;top:295px">
      <svg viewBox="0 0 62 62"><circle cx="31" cy="31" r="29" fill="none" stroke="#fff" stroke-width="2.5"/><path d="M19 44 V34 M25 44 V29 M31 44 V32 M37 44 V27 M43 44 V30" stroke="#fff" stroke-width="3.5"/><path d="M18 27 L25 21 L31 25 L37 19 L44 22" fill="none" stroke="#fff" stroke-width="2"/></svg>
      <span>Financial<br>Reporting</span>
    </div>
    <div class="service" style="left:56px;top:374px">
      <svg viewBox="0 0 62 62"><circle cx="31" cy="31" r="29" fill="none" stroke="#fff" stroke-width="2.5"/><path d="M16 31 L31 17 L46 31 M20 28 V45 H42 V28" fill="none" stroke="#fff" stroke-width="3" stroke-linejoin="round"/><text x="31" y="42" text-anchor="middle" font-family="Montserrat,sans-serif" font-weight="700" font-size="15" fill="#fff">$</text></svg>
      <span>Rent<br>Collection</span>
    </div>
    <div class="service" style="left:258px;top:374px">
      <svg viewBox="0 0 62 62"><circle cx="31" cy="31" r="29" fill="none" stroke="#fff" stroke-width="2.5"/><path d="M31 16 V44 M23 45 H39 M18 22 H44" stroke="#fff" stroke-width="2.5"/><path d="M14 33 L18 23 L22 33 Z M40 33 L44 23 L48 33 Z" fill="none" stroke="#fff" stroke-width="2"/><path d="M13 33 H23 A5 4 0 0 1 13 33 Z M39 33 H49 A5 4 0 0 1 39 33 Z" fill="#fff"/></svg>
      <span>Legal<br>Guidance</span>
    </div>
    <div class="service" style="left:56px;top:453px">
      <svg viewBox="0 0 62 62"><circle cx="31" cy="31" r="29" fill="none" stroke="#fff" stroke-width="2.5"/><circle cx="31" cy="31" r="11" fill="none" stroke="#fff" stroke-width="3" stroke-dasharray="5 3"/><path d="M19 20 L43 44" stroke="#fff" stroke-width="4.5" stroke-linecap="round"/></svg>
      <span>Maintenance</span>
    </div>
    <div class="service" style="left:258px;top:453px">
      <svg viewBox="0 0 62 62"><circle cx="31" cy="31" r="29" fill="none" stroke="#fff" stroke-width="2.5"/><path d="M31 15 L45 20 V31 C45 40 38 45 31 48 C24 45 17 40 17 31 V20 Z" fill="none" stroke="#fff" stroke-width="3" stroke-linejoin="round"/><path d="M31 20 V43" stroke="#fff" stroke-width="2"/></svg>
      <span>Evictions</span>
    </div>

    <div class="stamp-box"></div>
    <div class="address-line" style="top:214px"></div>
    <div class="address-line" style="top:240px"></div>
    <div class="address-line" style="top:265px"></div>
    <div class="address-line" style="top:291px"></div>

    <div class="contact">
      <div class="contact-title">CONTACT<br>OUR TEAM</div>
      <div class="contact-line">(806) 555-0142</div>
      <div class="contact-line">info@brightkeyrentals-example.com</div>
      <div class="contact-line">www.brightkeyrentals-example.com</div>
      <div class="contact-line">2287 Marble Lane, Lubbock, TX 79555</div>
    </div>
  </section>

</main>
</body>
</html>
```